Small scale cold brew coffee producer needs a label for its products

We are a cold brew coffee producer and am now going the next step and getting our products onto the retail market.
Cold brewed coffee is coffee that which is brewed over a long period of time so its coffee which is brewed opposed to boiled this allows for a smoother taste and removes the acidic taste note often experienced in hot normal coffee. We currently offer three varieties from this core product. The first being a ready to drink neat version, the second being coffee and milk and the final a coffee and coconut milk.
In terms of design of the label i am looking for an artisan style to maintain the craft nature of the product. yet possible the use of abstract art to increase the appeal of it on the shelf.
in terms of a message i am looking to portray one of the quality of our product such as no additives and the use of specialist grade coffee that is in season.
As a colour scheme i am pretty flexible except to that of bright blue and white as it has too much of a similarity to heath products.
The images below are possible ideas and my current logo

Target Market(s)

As i am using spiciest grade coffee this will create a high price point. Current consumption statistics suggest that the major consumption group is the 20 - 40 year olds working professional. Yet its a popular product in arty urban centers such as brighton and bristol

Industry/Entity Type

Retail

Font styles to use
Serif
Script

Requirements
Must have
• The use of graphics and images to better poetry the image for the product, yet i am still looking for a classical appearance so old school outer labels, but the most important feature will be to maintain the arazan appearance for the product
Nice to have
• If i could have a sharp contrast between the difference and the product so a sharp difference. Gentle colours which are not too sharp and bold but more mellow. Possible use of abstract art in the text to improve the overall apperance
Should not have
• modern sharp images as i want an old school type image, I don't want sharp whites, blues and reds as they are too closely related to the heath care

```html
<!DOCTYPE html>
<html lang="en">
<head>
<meta charset="utf-8">
<title>Marlowe's Cold Brewed Coffee – Original Label</title>
<link rel="stylesheet" href="https://fonts.googleapis.com/css2?family=Josefin+Sans:wght@400;600;700&family=Oswald:wght@700&display=swap">
<style>
  :root {
    --backdrop-light: #fbfbfb;
    --backdrop-dark: #e4e4e4;
    --label-cream: #fff4de;
    --accent-orange: #e57d45;
    --ink: #111111;
    --paper-white: #ffffff;
  }
  html, body {
    margin: 0;
    padding: 0;
    width: 1200px;
    height: 1000px;
    overflow: hidden;
  }
  body {
    background: radial-gradient(ellipse at center, var(--backdrop-light) 0%, var(--backdrop-dark) 85%);
    position: relative;
  }
  .bottle-label {
    position: absolute;
    left: 122px;
    top: 266px;
    width: 956px;
    height: 468px;
    box-shadow: 0 2px 6px rgba(0, 0, 0, 0.22);
  }
  .bottle-label svg { display: block; }
  .brand-name {
    font-family: "Josefin Sans", sans-serif;
    font-weight: 700;
    font-size: 44px;
    fill: var(--ink);
  }
  .ribbon-text {
    font-family: "Josefin Sans", sans-serif;
    font-weight: 700;
    font-size: 30px;
    letter-spacing: 2px;
    fill: var(--paper-white);
  }
  .product-type {
    font-family: "Josefin Sans", sans-serif;
    font-weight: 400;
    font-size: 27px;
    letter-spacing: 7px;
    fill: var(--ink);
  }
  .claim {
    font-family: "Oswald", sans-serif;
    font-weight: 700;
    fill: var(--ink);
  }
  .variant-name {
    font-family: "Josefin Sans", sans-serif;
    font-weight: 700;
    font-size: 25px;
    letter-spacing: 8px;
    fill: var(--label-cream);
  }
  .volume {
    font-family: "Josefin Sans", sans-serif;
    font-weight: 400;
    font-size: 13px;
    letter-spacing: 2px;
    fill: var(--ink);
  }
</style>
</head>
<body>
  <div class="bottle-label">
    <svg width="956" height="468" viewBox="0 0 956 468" xmlns="http://www.w3.org/2000/svg">
      <!-- label body -->
      <rect class="label-body" x="0" y="0" width="956" height="468" fill="var(--label-cream)"/>

      <!-- brand -->
      <circle class="brand-dot" cx="478" cy="30" r="14" fill="var(--accent-orange)"/>
      <text class="brand-name" x="478" y="92" text-anchor="middle">Marlowe's</text>

      <!-- ribbon banner -->
      <g class="ribbon">
        <polygon points="308,123 358,117 358,171 308,171 326,147" fill="var(--accent-orange)"/>
        <polygon points="648,123 598,117 598,171 648,171 630,147" fill="var(--accent-orange)"/>
        <rect x="338" y="116" width="280" height="48" fill="var(--accent-orange)"/>
        <line x1="344" y1="121" x2="612" y2="121" stroke="var(--label-cream)" stroke-width="1.5"/>
        <line x1="344" y1="159" x2="612" y2="159" stroke="var(--label-cream)" stroke-width="1.5"/>
        <text class="ribbon-text" x="478" y="152" text-anchor="middle">COLD BREWED</text>
      </g>

      <!-- product type -->
      <g class="product-line">
        <text x="383" y="193" font-size="14" text-anchor="middle" fill="var(--ink)">★</text>
        <text class="product-type" x="481" y="195" text-anchor="middle">COFFEE</text>
        <text x="573" y="193" font-size="14" text-anchor="middle" fill="var(--ink)">★</text>
      </g>

      <!-- quality claims -->
      <g class="claims">
        <line x1="324" y1="213" x2="632" y2="213" stroke="var(--ink)" stroke-width="2"/>
        <text class="claim" x="325" y="243" font-size="30" textLength="163" lengthAdjust="spacingAndGlyphs">MADE WITH</text>
        <text class="claim" x="325" y="272" font-size="30" textLength="163" lengthAdjust="spacingAndGlyphs">SPECIALIST</text>
        <text class="claim" x="325" y="313" font-size="46" textLength="163" lengthAdjust="spacingAndGlyphs">COFFEE</text>
        <line x1="497" y1="218" x2="497" y2="312" stroke="var(--ink)" stroke-width="2"/>
        <text class="claim" x="504" y="263" font-size="54" textLength="128" lengthAdjust="spacingAndGlyphs">100%</text>
        <text class="claim" x="504" y="313" font-size="54" textLength="126" lengthAdjust="spacingAndGlyphs">PURE</text>
        <line x1="324" y1="317" x2="632" y2="317" stroke="var(--ink)" stroke-width="2"/>
        <text class="claim" x="325" y="360" font-size="48" textLength="306" lengthAdjust="spacingAndGlyphs">NO ADDITIVES</text>
        <line x1="324" y1="366" x2="632" y2="366" stroke="var(--ink)" stroke-width="2"/>
      </g>

      <!-- variant band -->
      <rect class="variant-band" x="0" y="378" width="956" height="90" fill="var(--accent-orange)"/>
      <rect class="bean-pile" x="0" y="434" width="956" height="34" fill="var(--ink)" role="img" aria-label="Illustration of scattered roasted coffee beans along the bottom edge"/>
      <text class="variant-name" x="482" y="419" text-anchor="middle">ORIGINAL</text>
      <text class="volume" x="478" y="446" text-anchor="middle" fill="var(--label-cream)" style="fill: var(--label-cream)">12 fl oz (330ml)</text>
    </svg>
  </div>
</body>
</html>
```